PlumVerse Business Cards

I need a business card designed for PlumVerse. To get an idea of what we do please visit https://brisklayout.example/para-artistas-7

```html
<!DOCTYPE html>
<html lang="en">
<head>
<meta charset="utf-8">
<title>PlumVerse Business Cards</title>
<link rel="stylesheet" href="https://fonts.googleapis.com/css2?family=Montserrat:wght@300;400;500;700&display=swap">
<style>
  :root {
    --backdrop: #2b2b2b;
    --card-dark: #1f1f1f;
    --card-light: #ffffff;
    --accent: #e8931a;
    --ink: #1a1a1a;
    --rule-grey: #8a8a8a;
    --white: #ffffff;
  }
  * { box-sizing: border-box; margin: 0; padding: 0; }
  html, body {
    width: 1200px; height: 1186px; overflow: hidden;
    background: var(--backdrop);
    font-family: "Montserrat", sans-serif;
  }
  .card {
    position: absolute;
    width: 700px; height: 400px;
    border-radius: 24px;
    overflow: hidden;
    box-shadow: 0 18px 40px rgba(0,0,0,0.45);
  }
  .card-front { left: 60px; top: 130px; background: var(--card-dark); }
  .card-back  { left: 440px; top: 650px; background: var(--card-light); }

  .brand { position: absolute; display: flex; align-items: center; gap: 26px; }
  .brand-mark {
    border: 3px solid var(--accent);
    flex: none;
  }
  .brand-text { position: relative; }
  .brand-name {
    font-weight: 400;
    letter-spacing: 0.3em;
    text-transform: uppercase;
    line-height: 1;
  }
  .brand-rule {
    display: block;
    height: 1px;
    background: var(--rule-grey);
    margin-top: 8px;
  }
  .brand-tagline {
    display: block;
    color: var(--accent);
    font-weight: 500;
    letter-spacing: 0.35em;
    text-transform: uppercase;
    margin-top: 6px;
  }

  .card-front .brand { left: 70px; top: 150px; }
  .card-front .brand-mark { width: 96px; height: 96px; }
  .card-front .brand-name { color: var(--white); font-size: 38px; }
  .card-front .brand-tagline { font-size: 12px; }

  .card-back .brand { left: 50px; top: 60px; gap: 20px; }
  .card-back .brand-mark { width: 70px; height: 70px; }
  .card-back .brand-name { color: var(--ink); font-size: 28px; }
  .card-back .brand-tagline { font-size: 9px; }

  .person { position: absolute; left: 50px; top: 186px; }
  .person-name { color: var(--accent); font-weight: 700; font-size: 26px; line-height: 1.1; }
  .person-role { color: var(--ink); font-size: 16px; margin-top: 2px; }

  .divider {
    position: absolute; left: 50px; right: 40px; top: 252px;
    height: 2px; background: var(--accent);
  }

  .contacts { position: absolute; left: 50px; top: 266px; list-style: none; }
  .contacts li {
    display: flex; align-items: center; gap: 12px;
    font-size: 15px; color: var(--ink); line-height: 25px;
  }
  .contacts svg { width: 13px; height: 13px; fill: var(--accent); flex: none; }

  .address {
    position: absolute; right: 40px; top: 266px;
    text-align: right; font-size: 14px; color: var(--ink); line-height: 21px;
    font-style: normal;
  }
  .swoosh { position: absolute; left: 0; top: 0; width: 700px; height: 400px; }
</style>
</head>
<body>
  <section class="card card-front" aria-label="Card front">
    <div class="brand">
      <span class="brand-mark"></span>
      <div class="brand-text">
        <span class="brand-name">PlumVerse</span>
        <span class="brand-rule"></span>
        <span class="brand-tagline">Digital Notary</span>
      </div>
    </div>
  </section>

  <section class="card card-back" aria-label="Card back">
    <svg class="swoosh" viewBox="0 0 700 400" aria-hidden="true">
      <path d="M240 402 C300 384 470 384 530 374 C575 366 572 330 615 326 L700 326 L700 400 Z" fill="var(--accent)"/>
      <path d="M250 390 C310 374 470 372 530 362 C570 354 572 318 612 314 L700 314" fill="none" stroke="var(--ink)" stroke-width="6"/>
    </svg>

    <div class="brand">
      <span class="brand-mark"></span>
      <div class="brand-text">
        <span class="brand-name">PlumVerse</span>
        <span class="brand-rule"></span>
        <span class="brand-tagline">Digital Notary</span>
      </div>
    </div>

    <div class="person">
      <p class="person-name">Dana Reyes</p>
      <p class="person-role">CEO &amp; Founder</p>
    </div>

    <div class="divider"></div>

    <ul class="contacts">
      <li>
        <svg viewBox="0 0 24 24"><path d="M6.6 10.8a15.1 15.1 0 0 0 6.6 6.6l2.2-2.2a1 1 0 0 1 1-.25 11.4 11.4 0 0 0 3.6.57 1 1 0 0 1 1 1V20a1 1 0 0 1-1 1A17 17 0 0 1 3 4a1 1 0 0 1 1-1h3.5a1 1 0 0 1 1 1c0 1.25.2 2.45.57 3.57a1 1 0 0 1-.25 1z"/></svg>
        555 01 20 48
      </li>
      <li>
        <svg viewBox="0 0 24 24"><path d="M2 5h20v14H2z M2 5l10 8 10-8" /></svg>
        info@plumverse.example
      </li>
      <li>
        <svg viewBox="0 0 24 24"><circle cx="12" cy="12" r="10"/></svg>
        www.plumverse.example
      </li>
    </ul>

    <address class="address">
      Parque Norte, C/3 nº 18<br>
      4100 Villa Serena
    </address>
  </section>
</body>
</html>
```